Mardolin construction chemical business need advertisement

We need an advertisement as building signboard for a new company called "Mardolin"-meaning truly effective, value added building solution.
-we source the best and effective products around the world that suit the local climate conditions
- we carry varieties of quality construction chemicals products that are cost effective and suitable for any size of budget and project and even for home user DIY .
- we provide consultation and system to solve any building problems. e.g. tiling system, waterproofing system, concrete repair system, green roof system
- We provide products training and waterproofing solutions to our clients and applicators that use our products
-By utilising our products and services, will leverage the value of the properties and protect your investment.
-our mission- to provide consultancy, services to repair, to restpre and to add avlue to properties throughout the lifecycle of the building resulting in greater whole value hence not limited to develiper but to end user protecting their investment with the quality products and services we provide.
- our philosophy-"Passion towards commitment, quality, knowledge, good practice and result.
- we need the advertisement to be easily understand by End user and contractor of the service and product we provide to solve their problem
- yet also look professional to designer and architect
end user, contractor, builder, designer, achitect
Business
- -Please create a slogan, easily to understand at one glance of what type of service and products we provide.
- -less wording, the advertisement will be put at the building
- -Strong message to explain our business

```html
<!DOCTYPE html>
<html lang="en">
<head>
<meta charset="UTF-8">
<title>Mardolin Construction – Flyer</title>
<link rel="stylesheet" href="https://fonts.googleapis.com/css2?family=Anton&family=Baloo+2:wght@600;700&family=Montserrat:ital,wght@0,400;0,500;0,600;0,700;1,500&display=swap">
<style>
  :root{
    --red:#d7232a;
    --red-deep:#c21d24;
    --yellow:#f7e43a;
    --yellow-warm:#fbd622;
    --charcoal:#4a4a4a;
    --ink:#2b2b2b;
    --paper-top:#dcdddf;
    --paper-bottom:#ffffff;
    --stage:#f2f2f2;
  }
  *{box-sizing:border-box;margin:0;padding:0}
  html,body{width:1200px;height:1200px;overflow:hidden;background:var(--stage)}
  .flyer{
    position:absolute;left:176px;top:0;width:848px;height:1200px;overflow:hidden;
    background:linear-gradient(160deg,var(--paper-top) 0%,#eeeeef 55%,var(--paper-bottom) 100%);
    font-family:"Montserrat",sans-serif;color:var(--ink);
  }
  .flyer-shapes{position:absolute;inset:0;width:848px;height:1200px}

  .brand{
    position:absolute;right:34px;top:150px;text-align:right;
    font-family:"Anton",sans-serif;transform:skewX(-10deg);line-height:.95;
  }
  .brand-name{display:block;color:#fff;font-size:84px;letter-spacing:1px}
  .brand-sub{display:block;color:var(--yellow);font-size:45px;letter-spacing:1px}

  .hero-photo{
    position:absolute;left:42px;top:252px;width:336px;height:336px;border-radius:50%;
    background:linear-gradient(100deg,#a8673a 0%,#c98f5e 30%,#4a4a4a 45%,#5b5b5b 52%,#d39a66 62%,#b5784a 100%);
  }

  .slogan{
    position:absolute;left:500px;top:490px;width:330px;
    font-family:"Anton",sans-serif;line-height:1;
  }
  .slogan-lead{display:block;font-size:60px;color:#111;transform:skewX(-8deg)}
  .slogan-punch{display:block;font-size:68px;color:var(--red);transform:skewX(-8deg);margin-top:4px}
  .slogan-tag{
    display:block;margin-top:16px;font-family:"Montserrat",sans-serif;font-weight:500;
    font-size:26px;line-height:1.2;color:#111;
  }

  .tab{
    position:absolute;height:44px;display:flex;align-items:center;
    background:var(--red);color:var(--yellow);
    font-family:"Baloo 2",sans-serif;font-weight:700;font-size:28px;
    border-radius:22px;
  }
  .tab-about{left:22px;top:604px;width:300px;padding-left:36px}
  .tab-mission{right:0;top:730px;width:270px;padding-left:52px;border-radius:22px 0 0 22px}
  .tab-philosophy{right:0;top:922px;width:300px;padding-left:40px;border-radius:22px 0 0 22px}

  .about-list{
    position:absolute;left:40px;top:664px;width:420px;list-style:none;
    font-size:13.5px;font-weight:500;line-height:1.4;
  }
  .about-list li{position:relative;padding-left:14px;margin-bottom:10px}
  .about-list li::before{
    content:"";position:absolute;left:0;top:7px;width:5px;height:5px;border-radius:50%;background:var(--red);
  }

  .side-copy{
    position:absolute;right:30px;width:300px;text-align:right;
    font-size:13px;font-weight:500;font-style:italic;line-height:1.36;
  }
  .mission-copy{top:784px}
  .philosophy-copy{top:978px}
  .philosophy-copy p+p{margin-top:10px}

  .site-url{
    position:absolute;left:40px;top:1120px;color:#fff;font-size:16px;font-weight:500;
  }
  .partners{
    position:absolute;right:40px;top:1162px;display:flex;gap:26px;align-items:center;
  }
  .partner{color:#fff;font-family:"Montserrat",sans-serif;font-weight:700;font-size:15px}
</style>
</head>
<body>
<main class="flyer">
  <svg class="flyer-shapes" viewBox="0 0 848 1200" aria-hidden="true">
    <path d="M0 0 H848 V430 C500 200 250 80 0 80 Z" fill="var(--red)"/>
    <path d="M0 80 C250 80 500 200 848 430 V480 C500 250 250 128 0 128 Z" fill="var(--charcoal)"/>
    <path d="M0 136 C250 136 500 262 848 492 V520 C620 330 330 300 0 430 Z" fill="var(--red-deep)"/>
    <path d="M848 470 V718 H560 Q478 718 478 646 V570 Q478 490 560 470 Q700 440 848 470 Z" fill="var(--yellow)"/>
    <circle cx="204" cy="426" r="186" fill="var(--yellow-warm)"/>
    <circle cx="214" cy="418" r="178" fill="var(--red)"/>
    <path d="M0 996 C250 1106 560 1156 848 1146" fill="none" stroke="var(--yellow)" stroke-width="10"/>
    <path d="M0 1004 C250 1114 560 1164 848 1154 V1200 H0 Z" fill="var(--red)"/>
  </svg>

  <div class="brand">
    <span class="brand-name">MARDOLIN</span>
    <span class="brand-sub">CONSTRUCTION</span>
  </div>

  <div class="hero-photo" role="img" aria-label="Close-up photo of a gloved hand setting ceramic wall tiles onto notched tile adhesive"></div>

  <div class="slogan">
    <span class="slogan-lead">IF YOU DO IT</span>
    <span class="slogan-punch">DO IT RIGHT</span>
    <span class="slogan-tag">Everything you need<br>from start to finish</span>
  </div>

  <h2 class="tab tab-about">About Us</h2>
  <ul class="about-list">
    <li>We source the best and effective products around the world that suit the local climate conditions.</li>
    <li>We carry varieties of quality construction chemicals products that are cost effective and suitable for any size of budget and project and even for home user DIY.</li>
    <li>We provide consultation and system to solve any building problems. e.g. tiling system, waterproofing system, concrete repair system, green roof system.</li>
    <li>We provide products training and waterproofing solutions to our clients and applicators that use our products.</li>
    <li>By utilising our products and services, will leverage the value of the properties and protect your investment.</li>
  </ul>

  <h2 class="tab tab-mission">Our Mission</h2>
  <p class="side-copy mission-copy">To provide consultancy, services to repair, to restpre and to add avlue to properties throughout the lifecycle of the building resulting in greater whole value hence not limited to develiper but to end user protecting their investment with the quality products and services we provide.</p>

  <h2 class="tab tab-philosophy">Our Philosophy</h2>
  <div class="side-copy philosophy-copy">
    <p>Passion towards commitment, quality, knowledge, good practice and result.</p>
    <p>We need the advertisement to be easily understand by End user and contractor of the service and product we provide to solve their problem</p>
  </div>

  <p class="site-url">www.website.com</p>
  <div class="partners">
    <span class="partner">Ferrobond</span>
    <span class="partner">Kelva</span>
    <span class="partner">Torvane</span>
  </div>
</main>
</body>
</html>
```